Business Card design for Founder and CEO of new shoe company

I am looking for a business card design for my new shoe company called Strapwell.

I am launching the company this April. Strapwell shoes offers slip-on athletic and casual style shoes for men and women. The unique selling point of the brand is that all of our shoe exist without shoelaces. I have included a link to the website to offer additional information about the company, see product images, and gain inspiration for the design. You can use the store owner password "Strapwell" to access the website.

www.Strapwell.example

Thanks,
Dan Hollis

Target Market(s)

Active Men and Women ages 16-45

Industry/Entity Type

Business

Contact Information for Business Card

Dan Hollis
Founder and CEO
www.Strapwell.example
danhollis@Strapwell.example
888-555-0187 / 888-5STRAPW
Strapwell, LLC
2284 N Tamsin Ave
Chicago, IL 60699

Requirements
Must have
• Be able to quickly and easily tell that Strapwell is a shoe company from the business card

```html
<!DOCTYPE html>
<html lang="en">
<head>
<meta charset="utf-8">
<title>Strapwell Business Card</title>
<link href="https://fonts.googleapis.com/css2?family=Questrial&display=swap" rel="stylesheet">
<style>
  :root {
    --backdrop: #d1d2d4;
    --brand-blue: #1390c8;
    --band-gray: #b0bbb3;
    --ink: #111111;
    --paper: #ffffff;
    --frame: #b9c2bd;
  }
  html, body {
    margin: 0;
    padding: 0;
    overflow: hidden;
  }
  body {
    width: 1199px;
    height: 1200px;
    background: var(--backdrop);
    position: relative;
    font-family: "Questrial", "Century Gothic", sans-serif;
    color: var(--ink);
  }
  .card {
    position: absolute;
    left: 146px;
    width: 906px;
    height: 517px;
    box-shadow: 8px 8px 6px rgba(0,0,0,0.45);
    overflow: hidden;
  }
  .card--front { top: 67px; background: var(--paper); }
  .card--back { top: 615px; height: 518px; background: var(--brand-blue); }

  .band { position: absolute; left: 0; width: 100%; }
  .band--blue { background: var(--brand-blue); }
  .band--gray { background: var(--band-gray); }

  .front-top { top: 0; height: 32px; }
  .front-header { top: 32px; height: 100px; display: flex; align-items: center; justify-content: center; gap: 18px; }
  .front-bottom { bottom: 0; height: 32px; }

  .wordmark { font-size: 62px; line-height: 1; letter-spacing: 1px; }
  .wordmark-square { width: 34px; height: 34px; background: var(--ink); }

  .holder { position: absolute; left: 33px; top: 277px; }
  .holder-name { font-size: 35px; line-height: 1; margin: 0; font-weight: 400; }
  .holder-title { font-size: 18px; margin: 4px 0 0; }

  .contact {
    position: absolute; left: 615px; top: 153px;
    font-size: 21px; line-height: 25px; margin: 0; padding: 0; list-style: none;
  }

  .gallery { position: absolute; top: 343px; left: 34px; display: flex; gap: 11px; }
  .gallery-item {
    width: 199px; height: 133px; border: 2px solid var(--frame);
  }
  .shoe-pink { background: radial-gradient(ellipse at 50% 60%, #4a5fc8 0%, #d64aa8 45%, #f4f4f4 75%); }
  .shoe-gray { background: radial-gradient(ellipse at 50% 60%, #5a5a5a 0%, #6e6e6e 40%, #e8763a 55%, #f2f2f2 78%); }
  .shoe-cyan { background: radial-gradient(ellipse at 50% 60%, #2aa6dc 0%, #a9b4ba 45%, #f4f4f4 78%); }
  .shoe-blue { background: linear-gradient(180deg, #f4f4f4 0%, #3aa3e0 45%, #1e88cf 65%, #2b2b2b 100%); }

  .back-logo {
    position: absolute; top: 215px; left: 0; width: 100%;
    display: flex; align-items: center; justify-content: center; gap: 22px;
    color: var(--paper);
  }
  .back-logo .wordmark { font-size: 82px; }
  .back-logo .wordmark-square { width: 44px; height: 44px; background: var(--paper); }
  .back-url-band { top: 454px; height: 32px; display: flex; align-items: center; justify-content: center; font-size: 24px; }
</style>
</head>
<body>
  <section class="card card--front">
    <div class="band band--blue front-top"></div>
    <header class="band band--gray front-header">
      <span class="wordmark-square"></span>
      <span class="wordmark">Strapwell</span>
    </header>

    <div class="holder">
      <h1 class="holder-name">Dan Hollis</h1>
      <p class="holder-title">Founder and CEO</p>
    </div>

    <ul class="contact">
      <li>www.Strapwell.example</li>
      <li>danhollis@Strapwell.example</li>
      <li>888-555-0187</li>
      <li>888-5STRAPW</li>
      <li>Strapwell, LLC</li>
      <li>2284 N Tamsin Ave</li>
      <li>Chicago, IL 60699</li>
    </ul>

    <div class="gallery">
      <div class="gallery-item shoe-pink" role="img" aria-label="Photo of a blue and pink laceless athletic shoe"></div>
      <div class="gallery-item shoe-gray" role="img" aria-label="Photo of a gray and orange laceless athletic shoe"></div>
      <div class="gallery-item shoe-cyan" role="img" aria-label="Photo of a cyan and gray laceless athletic shoe"></div>
      <div class="gallery-item shoe-blue" role="img" aria-label="Photo of a blue and black laceless athletic shoe"></div>
    </div>

    <div class="band band--blue front-bottom"></div>
  </section>

  <section class="card card--back">
    <div class="back-logo">
      <span class="wordmark-square"></span>
      <span class="wordmark">Strapwell</span>
    </div>
    <div class="band band--gray back-url-band">www.Strapwell.example</div>
  </section>
</body>
</html>
```